Biz card for my counselling/social work practice

Biz card design for my counselling practice, focus on well-being, I am a social worker who also teaches meditation and workshops but my main focus for the card is my counselling practice. My website reveals a gentle flowing quality which I would life reflected in my card. This business card will be designed to share with other practitioners who are looking for support with their clients to take their healing to another level or well-being.

Target Market(s)

professionals seeking mental health counselling/men/women/ those seeking to improve their well-being through insight based counselling to optimize their lives and process trauma or limiting patterns

Industry/Entity Type

Counsellor

Contact Information for Business Card

Info on the card: perhaps text is aligned left?
Marla Finch, MSW, RSW
Counsellor
250.555.0142
info@marlafinch.ca
www.marlafinch.ca

Please use a modern font doesn’t need to be the one chosen below. Thank you

Font styles to use
Serif

Colors
3176b5
33a6d7
33b8a4
6b449b
abd037
d2a4cc
e55fa2

Requirements
Must have
• My business card details on front
• Backside
• Accelerated Resolution Therapy
• Cognitive Behavioral Therapy
• Mindfulness Informed Therapy
Nice to have
• I would like the card to be basic, (white or creme without too much bold colour) and with perhaps a stripe or band of vertical colour in blue or green (or a merge of colour) perhaps embossed or in a negative space. (this is one idea, but do not want the card to be too feminine or interest only women as i see men too so this is only an idea, but not 100 percent on this.
• I do not have a logo. I would prefer to heart from my website not to be used in the design as i am considering modifying this and re-branding.
Should not have
• too bold colours or bright yellow/blacks. i Like tones that are greens, blues.

```html
<!DOCTYPE html>
<html lang="en">
<head>
<meta charset="utf-8">
<title>Marla Finch Counselling — Business Card</title>
<link rel="stylesheet" href="https://fonts.googleapis.com/css2?family=Raleway:wght@400;500&family=Source+Sans+3:wght@400&display=swap">
<style>
  :root {
    --paper: #ffffff;
    --frame: #8a8a8a;
    --ink: #6a6a6a;
    --ink-strong: #5f5f5f;
    --band-sky: #bcd8e5;
    --band-teal: #88c6c4;
    --band-slate: #88bbc7;
    --band-text: #ffffff;
    --wash-lilac: #dbd4e5;
    --wash-aqua: #d9f4f4;
  }
  * { margin: 0; padding: 0; box-sizing: border-box; }
  html, body {
    width: 1200px; height: 533px; overflow: hidden;
    background: var(--paper);
  }
  .sheet { position: relative; width: 1200px; height: 533px; }
  .card {
    position: absolute; top: 115px;
    width: 519px; height: 307px;
    border: 1px solid var(--frame);
    background: var(--paper);
    overflow: hidden;
  }
  .card--back { left: 52px; }
  .card--front { left: 615px; }

  .modalities {
    position: absolute; left: -1px; top: -1px;
    width: 519px; height: 307px;
  }
  .modality-band--art { fill: var(--band-sky); }
  .modality-band--cbt { fill: var(--band-teal); }
  .modality-band--mit { fill: var(--band-slate); }
  .modality-label {
    font-family: "Source Sans 3", sans-serif;
    fill: var(--band-text);
  }

  .colour-wash {
    position: absolute; left: 0; top: 0; width: 162px; height: 100%;
    background: linear-gradient(to right, var(--wash-lilac), var(--wash-aqua));
  }
  .contact {
    position: absolute; left: 201px; top: 52px;
    list-style: none;
    font-family: "Raleway", sans-serif;
    color: var(--ink);
    font-size: 23px;
    white-space: nowrap;
  }
  .contact li { height: 40.6px; line-height: 40.6px; }
  .contact .name { font-weight: 500; color: var(--ink-strong); }
</style>
</head>
<body>
<main class="sheet">
  <section class="card card--back" aria-label="Card back: therapies offered">
    <svg class="modalities" viewBox="0 0 519 307" aria-hidden="false">
      <rect class="modality-band--art" x="0" y="71" width="519" height="50"/>
      <rect class="modality-band--cbt" x="0" y="132" width="519" height="50"/>
      <rect class="modality-band--mit" x="0" y="193" width="519" height="50"/>
      <text class="modality-label" x="41" y="103.5" font-size="21" textLength="432" lengthAdjust="spacing">ACCELERATED RESOLUTION THERAPY</text>
      <text class="modality-label" x="41" y="166" font-size="23" textLength="432" lengthAdjust="spacing">COGNITIVE BEHAVIORAL THERAPY</text>
      <text class="modality-label" x="41" y="225.5" font-size="22" textLength="432" lengthAdjust="spacing">MINDFULNESS INFORMED THERAPY</text>
    </svg>
  </section>
  <section class="card card--front" aria-label="Card front: contact details">
    <div class="colour-wash"></div>
    <ul class="contact">
      <li class="name">Marla Finch, MSW, RSW</li>
      <li>Counsellor</li>
      <li>250.555.0142</li>
      <li>info@marlafinch.ca</li>
      <li>www.marlafinch.ca</li>
    </ul>
  </section>
</main>
</body>
</html>
```